Bref créative
KORVO FREIGHT
BUSINESS CARDS AND BROCHURE LAYOUT
Professional
Reed Quandt
Owner/Specialist
I want no address
korvofreight@nubramail.com
www.korvofreight-example.com
just the logo on the back

```html
<!DOCTYPE html>
<html lang="en">
<head>
<meta charset="utf-8">
<title>Korvo Freight — Trifold Brochure</title>
<link rel="stylesheet" href="https://fonts.googleapis.com/css2?family=Open+Sans:wght@400;600;700;800&display=swap">
<style>
  :root{
    --red:#c8202a;
    --red-dark:#9e1219;
    --ink:#2b2b2b;
    --grey:#6d6d6d;
    --paper:#ffffff;
    --stage:#e7e4e0;
    --photo-a:#b9b4ae;
    --photo-b:#7e7870;
  }
  *{box-sizing:border-box;margin:0;padding:0}
  html,body{width:1200px;height:474px;overflow:hidden}
  body{background:var(--stage);font-family:"Open Sans",Arial,sans-serif;color:var(--ink);position:relative}
  .spread{position:absolute;top:72px;width:552px;height:330px;display:flex;background:var(--paper);box-shadow:0 4px 14px rgba(0,0,0,.18)}
  .spread--outside{left:30px}
  .spread--inside{left:618px}
  .panel{position:relative;width:184px;height:330px;overflow:hidden;border-right:1px solid #eee}
  .panel:last-child{border-right:none}
  .photo{position:absolute;background:linear-gradient(150deg,var(--photo-a),var(--photo-b))}
  .tab{position:absolute;background:var(--red);color:#fff;font-weight:700;font-size:7.5px;letter-spacing:.4px;padding:4px 8px;line-height:1.2;text-transform:uppercase}
  .copy{position:absolute;font-size:4.6px;line-height:1.55;color:var(--grey)}
  .copy p+p{margin-top:4px}
  .service-list{position:absolute;list-style:none;font-size:4.8px;line-height:2;color:var(--grey)}
  .service-list li::before{content:"";display:inline-block;width:3px;height:3px;background:var(--red);margin-right:4px;vertical-align:middle}
  .swoosh{position:absolute;left:0;width:100%}
  .brand{position:absolute;display:flex;align-items:center;gap:5px;font-weight:800;color:var(--red);white-space:nowrap}
  .brand__mark{background:var(--red)}
  .tagline{position:absolute;width:100%;text-align:center;font-size:4.4px;color:var(--grey);letter-spacing:.6px}
  .contact{position:absolute;list-style:none;font-size:5px;line-height:2.1;color:var(--grey)}
  .contact svg{width:6px;height:6px;vertical-align:middle;margin-right:4px;fill:var(--red)}
  .feature-box{position:absolute;left:14px;width:156px;height:44px;border:1px solid var(--red);padding:5px 6px 5px 62px;font-size:4.6px;line-height:1.5;color:var(--grey)}
  .feature-box .photo{left:4px;top:4px;width:52px;height:34px}
</style>
</head>
<body>

<section class="spread spread--outside" aria-label="Brochure outside">
  <article class="panel panel--services">
    <div class="photo" role="img" aria-label="Photo of a delivery truck on the road" style="left:0;top:0;width:184px;height:70px"></div>
    <div class="tab" style="right:0;top:62px">Services</div>
    <ul class="service-list" style="left:62px;top:82px">
      <li>Same-day local delivery</li>
      <li>Pallet and freight hauling</li>
      <li>Tracked parcel courier</li>
      <li>Office and home moves</li>
      <li>Scheduled business routes</li>
    </ul>
    <div class="tab" style="left:0;top:138px">About us</div>
    <div class="copy" style="left:12px;top:160px;width:160px">
      <p>We move parcels, pallets and full loads across the region with tracked vans, careful drivers and clear pricing. Every shipment is handled with care from pickup to doorstep.</p>
      <p>We move parcels, pallets and full loads across the region with tracked vans, careful drivers and clear pricing. Every shipment is handled with care from pickup to doorstep.</p>
      <p>We move parcels, pallets and full loads across the region with tracked vans, careful drivers and clear pricing.</p>
    </div>
  </article>

  <article class="panel panel--contact">
    <svg class="swoosh" style="top:0" viewBox="0 0 184 60" height="60" preserveAspectRatio="none" aria-hidden="true">
      <path d="M0 20 Q90 60 184 24 L184 0 L0 0Z" fill="#fff"/>
      <path d="M0 26 Q90 64 184 30" stroke="var(--red)" stroke-width="3" fill="none"/>
    </svg>
    <ul class="contact" style="left:56px;top:134px">
      <li><svg viewBox="0 0 10 10"><path d="M2 1l2 2-1 1.5c.6 1.2 1.4 2 2.5 2.5L7 6l2 2-1.5 1.5C4.5 9 1 5.5.5 2.5Z"/></svg>+1 555 0142 880</li>
      <li><svg viewBox="0 0 10 10"><path d="M1 2h8v6H1Zm0 0 4 3 4-3" stroke="var(--red)" fill="none"/></svg>korvofreight@nubramail.com</li>
      <li><svg viewBox="0 0 10 10"><circle cx="5" cy="5" r="4" stroke="var(--red)" fill="none"/></svg>www.korvofreight-example.com</li>
    </ul>
    <div class="photo" role="img" aria-label="Illustration of a hand truck stacked with cardboard boxes" style="left:20px;top:186px;width:110px;height:110px;background:linear-gradient(160deg,#d4b48a,#8c6a44)"></div>
    <svg class="swoosh" style="bottom:0" viewBox="0 0 184 70" height="70" preserveAspectRatio="none" aria-hidden="true">
      <path d="M0 40 Q100 10 184 50 L184 70 L0 70Z" fill="var(--red)"/>
      <path d="M0 30 Q100 0 184 40" stroke="#333" stroke-width="3" fill="none"/>
    </svg>
  </article>

  <article class="panel panel--cover">
    <div class="brand" style="left:34px;top:138px;font-size:14px">
      <span class="brand__mark" style="width:10px;height:10px;border-radius:50%"></span>KORVO FREIGHT
    </div>
    <div class="tagline" style="top:160px">FAST · SAFE · ON TIME DELIVERY</div>
    <svg class="swoosh" style="bottom:0" viewBox="0 0 184 90" height="90" preserveAspectRatio="none" aria-hidden="true">
      <path d="M0 60 Q100 10 184 30 L184 90 L0 90Z" fill="var(--red)"/>
      <path d="M0 48 Q100 0 184 20" stroke="#333" stroke-width="3" fill="none"/>
    </svg>
  </article>
</section>

<section class="spread spread--inside" aria-label="Brochure inside">
  <article class="panel panel--advance-one">
    <svg class="swoosh" style="top:0" viewBox="0 0 184 60" height="60" preserveAspectRatio="none" aria-hidden="true">
      <path d="M0 0 L60 0 Q20 20 0 50Z" fill="var(--red)"/>
    </svg>
    <div class="tab" style="left:0;top:22px">Advancement<br>in business</div>
    <div class="copy" style="left:14px;top:58px;width:158px">
      <p>We move parcels, pallets and full loads across the region with tracked vans, careful drivers and clear pricing. Every shipment is handled with care from pickup to doorstep.</p>
      <p>We move parcels, pallets and full loads across the region with tracked vans, careful drivers and clear pricing. Every shipment is handled with care from pickup to doorstep.</p>
    </div>
    <div class="photo" role="img" aria-label="Photo of boxes being loaded into a van" style="left:14px;top:190px;width:156px;height:110px"></div>
  </article>

  <article class="panel panel--advance-two">
    <div class="tab" style="left:0;top:22px">Advancement<br>in business</div>
    <div class="copy" style="left:14px;top:58px;width:158px">
      <p>We move parcels, pallets and full loads across the region with tracked vans, careful drivers and clear pricing. Every shipment is handled with care from pickup to doorstep.</p>
      <p>We move parcels, pallets and full loads across the region with tracked vans, careful drivers and clear pricing. Every shipment is handled with care from pickup to doorstep.</p>
    </div>
    <div class="photo" role="img" aria-label="Photo of a delivery van at a loading dock" style="left:14px;top:160px;width:156px;height:92px"></div>
    <div class="brand" style="left:44px;top:276px;font-size:10px">
      <span class="brand__mark" style="width:7px;height:7px;border-radius:50%"></span>KORVO FREIGHT
    </div>
    <svg class="swoosh" style="bottom:0" viewBox="0 0 184 30" height="30" preserveAspectRatio="none" aria-hidden="true">
      <path d="M0 20 Q92 0 184 20 L184 30 L0 30Z" fill="var(--red)"/>
    </svg>
  </article>

  <article class="panel panel--features">
    <svg class="swoosh" style="top:0" viewBox="0 0 184 60" height="60" preserveAspectRatio="none" aria-hidden="true">
      <path d="M0 0 L184 0 L184 40 Q90 10 0 20Z" fill="var(--red)"/>
      <path d="M0 26 Q90 16 184 46" stroke="#333" stroke-width="2" fill="none"/>
    </svg>
    <div class="tab" style="right:0;top:58px;background:var(--red-dark)">Features</div>
    <div class="feature-box" style="top:88px">
      <div class="photo" role="img" aria-label="Photo of a white cargo van"></div>
      Same-day routes, tracked from start to finish.
    </div>
    <div class="feature-box" style="top:144px">
      <div class="photo" role="img" aria-label="Photo of a courier carrying a parcel"></div>
      Same-day routes, tracked from start to finish.
    </div>
    <div class="feature-box" style="top:200px">
      <div class="photo" role="img" aria-label="Photo of stacked freight boxes"></div>
      Same-day routes, tracked from start to finish.
    </div>
    <svg class="swoosh" style="bottom:0" viewBox="0 0 184 50" height="50" preserveAspectRatio="none" aria-hidden="true">
      <path d="M0 30 Q100 0 184 26 L184 50 L0 50Z" fill="var(--red)"/>
    </svg>
  </article>
</section>

</body>
</html>
```